Fernhollow Services

After a high quality design website. we are a company that provides services to people that own land and need a hand getting on top of the delayed jobs.
would want a number of tab/ pages for the web page.
Home page / About us page / services page / Gallery page. / Contact us page
we offer a wide range of services .listed below

Stock Work (title)

Stock movement
Break feeding
Temporary staffing

Spraying (title)

Spraying weeds
Spraying gorse

Pastures (title)

Fertilizing
Topping

Building (title)

Habitable sheds
Farm sheds
Sheep yards
Cattle yards
Repair farm buildings
Decks
Retaining walls

Fencing (title)

Stock fencing
Post & rail
Stock yards repair
Electric fencing install & repairs

Water Management (title)

Water trough installation
Water scheme install
Water trough cleaning
Farm water maintenance
Water ponds
Ornamental ponds
Drainage

General (title)

Lawn mowing
Hedge trimming
Pruning trees
Metaling drive ways & races
Water blasting
Small digger work
Little tip truck cartage
Home kill management
Mulching gorse
Section clearing

```html
<!DOCTYPE html>
<html lang="en">
<head>
<meta charset="utf-8">
<title>Fernhollow Services</title>
<link href="https://fonts.googleapis.com/css2?family=Poppins:wght@400;500;600;700;800&display=swap" rel="stylesheet">
<style>
:root{
  --green:#5c9c13;
  --green-dark:#3f7309;
  --ink:#1e1e1e;
  --text:#555;
  --light:#f4f4f4;
  --footer:#222;
  --white:#fff;
}
*{margin:0;padding:0;box-sizing:border-box}
html,body{width:1200px;height:3716px;overflow:hidden}
body{font-family:'Poppins',sans-serif;color:var(--ink);background:var(--white);position:relative}
.abs{position:absolute}
.btn{position:absolute;display:flex;align-items:center;justify-content:center;background:var(--green);color:var(--white);font-weight:700;font-size:16px;letter-spacing:.3px;box-shadow:5px 5px 0 var(--ink);text-transform:uppercase}
.btn.dark{background:var(--ink);box-shadow:5px 5px 0 #3d3d3d}

/* top bar */
.topline{left:0;top:0;width:1200px;height:7px;background:#2b2b2b}
.topbar{left:690px;top:0;width:510px;height:52px;background:#2b2b2b;clip-path:polygon(0 0,100% 0,100% 100%,32px 100%);color:var(--white);font-size:16px;display:flex;align-items:center;gap:18px;padding-left:42px}
.topbar span{display:flex;align-items:center;gap:7px}
.topbar b{font-weight:600}

/* header */
.brand{display:flex;align-items:center;gap:12px}
.brand i{width:22px;height:22px;border-radius:50%;background:var(--green);display:block;flex:none}
.brand span{font-size:27px;font-weight:600;color:var(--green);line-height:1;white-space:nowrap}
.header-brand{left:75px;top:62px}
.nav{font-size:14.5px;font-weight:600;color:#333}
.nav a{position:absolute;white-space:nowrap;color:inherit;text-decoration:none}
.nav a.active{color:var(--green)}
.quote{left:945px;top:75px;width:183px;height:48px;font-size:15px}

/* hero */
.hero{left:0;top:144px;width:1200px;height:593px;background:linear-gradient(180deg,#d6dccd 0%,#b7c2a9 28%,#7c9254 50%,#5d7a2e 72%,#4b6622 100%)}
.hero-tractor{left:760px;top:260px;width:280px;height:210px;border-radius:30px;background:radial-gradient(ellipse at center,rgba(40,90,40,.55),rgba(40,90,40,0) 70%)}
.hero-copy{left:75px;top:272px;color:var(--white)}
.hero-copy .pre{font-size:38px;font-weight:800;line-height:1;letter-spacing:.5px}
.hero-copy h1{font-size:66px;font-weight:800;line-height:.82;margin-top:6px;letter-spacing:.5px}
.hero-copy p{font-size:23px;font-weight:700;line-height:30px;width:500px;margin-top:14px}
.hero-btn{left:75px;top:545px;width:185px;height:58px}
.dots{left:75px;top:679px;display:flex;gap:8px}
.dots i{width:29px;height:4px;background:rgba(255,255,255,.35);display:block}
.dots i:first-child{background:var(--white)}

/* services */
.sec-title{font-size:50px;font-weight:800;text-align:center;width:1200px;left:0;letter-spacing:.5px}
.tabs{left:0;top:875px;width:1200px;height:42px}
.tabs span{position:absolute;top:12px;font-size:14.5px;font-weight:600;color:#333;white-space:nowrap}
.tabs .on{top:0;height:42px;border:2px solid var(--green);color:var(--green);padding:0 14px;display:flex;align-items:center}
.card{top:955px;width:328px;height:401px;border:3px solid #d5d5d5;border-top:0;background:var(--white)}
.card .ph{height:202px;margin:0 -3px}
.card h3{margin-top:30px;text-align:center;color:var(--green);font-size:20px;font-weight:700}
.card p{text-align:center;font-size:13.5px;line-height:24px;color:var(--text);padding:0 18px;margin-top:10px}
.card .go{position:absolute;left:50%;bottom:-24px;margin-left:-24px;width:48px;height:48px;border-radius:50%;background:var(--ink);border:3px solid var(--white);box-shadow:0 0 0 2px #cfcfcf;display:flex;align-items:center;justify-content:center}
.arrow{top:1134px}

/* about */
.about{left:0;top:1444px;width:1200px;height:595px;background:linear-gradient(180deg,#2f3528 0%,#3a4030 45%,#3b4422 75%,#2f3818 100%)}
.about-ring{left:116px;top:1523px;width:438px;height:438px;border-radius:50%;border:5px solid #cfcfcf}
.about-img{left:126px;top:1533px;width:418px;height:418px;border-radius:50%;background:linear-gradient(150deg,#7d8790 0%,#a9a49a 40%,#8b8c86 70%,#5c5e58 100%)}
.about-copy{left:617px;top:1550px;color:var(--white);width:560px}
.about-copy h2{font-size:50px;font-weight:800;line-height:48px;letter-spacing:.3px;white-space:nowrap}
.about-copy p{font-size:16px;line-height:29px;margin-top:24px;width:510px}
.about-btn{position:relative;display:flex;width:182px;height:54px;margin-top:26px}

/* gallery */
.g{position:absolute}
.view{left:509px;top:2657px;width:183px;height:55px}

/* contact */
.contact{left:0;top:2798px;width:1200px;height:551px;background:var(--green)}
.contact-ph{left:75px;top:2870px;width:512px;height:406px;background:linear-gradient(135deg,#c9ccc8 0%,#9ea3a0 45%,#6f7472 75%,#505553 100%)}
.contact h2{position:absolute;left:616px;top:58px;color:var(--white);font-size:50px;font-weight:800;letter-spacing:.5px;line-height:1}
.field{position:absolute;background:var(--white);border:1px solid #ddd;font-size:13.5px;color:#777;padding:14px 14px}
.submit{left:616px;top:3228px;width:177px;height:49px;font-size:16px}

/* footer */
.footer{left:0;top:3349px;width:1200px;height:367px;background:var(--footer);color:var(--white)}
.footer h4{position:absolute;font-size:16px;font-weight:700;letter-spacing:.3px}
.footer .links{position:absolute;font-size:14px;line-height:32.6px}
.footer .copy{position:absolute;left:75px;top:206px;font-size:13px;line-height:21px}
.addr{position:absolute;left:886px;font-size:13.5px;line-height:28px;display:flex;gap:14px}
.addr svg{flex:none;margin-top:7px}
.social{position:absolute;left:886px;top:241px;display:flex;gap:14px}
.social i{width:22px;height:22px;border-radius:50%;border:2px solid var(--white);display:block}
</style>
</head>
<body>

<div class="abs topline"></div>
<div class="abs topbar">
  <span><svg width="14" height="14" viewBox="0 0 24 24"><path fill="#5c9c13" d="M6.6 10.8a15.1 15.1 0 0 0 6.6 6.6l2.2-2.2a1 1 0 0 1 1-.25 11.4 11.4 0 0 0 3.6.57 1 1 0 0 1 1 1V20a1 1 0 0 1-1 1A17 17 0 0 1 3 4a1 1 0 0 1 1-1h3.5a1 1 0 0 1 1 1c0 1.25.2 2.45.57 3.57a1 1 0 0 1-.25 1z"/></svg><b>+64-555-0142</b></span>
  <span><svg width="14" height="12" viewBox="0 0 24 18"><rect width="24" height="18" rx="2" fill="#5c9c13"/><path d="M1 2l11 8 11-8" stroke="#2b2b2b" stroke-width="2" fill="none"/></svg>hello@fernhollow.example</span>
</div>

<header>
  <div class="abs brand header-brand"><i></i><span>Fernhollow Services</span></div>
  <nav class="abs nav" style="left:0;top:90px">
    <a class="active" style="left:427px">HOME</a>
    <a style="left:505px">ABOUT US</a>
    <a style="left:614px">SERVICES</a>
    <a style="left:720px">GALLERY</a>
    <a style="left:818px">CONTACT US</a>
  </nav>
  <div class="btn quote">Request a Quote</div>
</header>

<section>
  <div class="abs hero" role="img" aria-label="Green tractor working a wide crop field with hills behind"></div>
  <div class="abs hero-tractor"></div>
  <div class="abs hero-copy">
    <div class="pre">WELCOME TO</div>
    <h1>FERNHOLLOW<br>SERVICES</h1>
    <p>We provides services to people that own land and need a hand getting on top of the delayed jobs.</p>
  </div>
  <div class="btn hero-btn">Contact Us</div>
  <div class="abs dots"><i></i><i></i><i></i><i></i></div>
</section>

<section>
  <h2 class="abs sec-title" style="top:790px">OUR SERVICES</h2>
  <div class="abs tabs">
    <span style="left:176px">STOCK WORK</span>
    <span style="left:316px">SPRAYING</span>
    <span style="left:430px">PASTURES</span>
    <span style="left:543px">BUILDING</span>
    <span style="left:651px">FENCING</span>
    <span style="left:755px">WATER MANAGEMENT</span>
    <span class="on" style="left:940px">GENERAL</span>
  </div>

  <svg class="abs arrow" style="left:32px" width="30" height="42" viewBox="0 0 30 42"><path d="M24 4L8 21l16 17" stroke="#111" stroke-width="7" fill="none"/></svg>
  <svg class="abs arrow" style="left:1138px" width="30" height="42" viewBox="0 0 30 42"><path d="M6 4l16 17L6 38" stroke="#111" stroke-width="7" fill="none"/></svg>

  <article class="abs card" style="left:74px">
    <div class="ph" role="img" aria-label="Person pushing a lawn mower across a sunny lawn" style="background:linear-gradient(180deg,#b9c77a 0%,#7ea33e 55%,#4f7d22 100%)"></div>
    <h3>LAWN MOWING</h3>
    <p>Excepteur sint occaecat cupidatat non proident, sunt in culpa qui officia deserunt mollit anim id est laborum aute irure dolor aliquip ex ea commodo.</p>
    <div class="go"><svg width="14" height="18" viewBox="0 0 14 18"><path d="M3 2l8 7-8 7" stroke="#fff" stroke-width="3.5" fill="none"/></svg></div>
  </article>
  <article class="abs card" style="left:436px">
    <div class="ph" role="img" aria-label="Gardener trimming a long green hedge" style="background:linear-gradient(160deg,#9fb87a 0%,#4f8a26 45%,#2f6a18 100%)"></div>
    <h3>HEDGE TRIMMING</h3>
    <p>Excepteur sint occaecat cupidatat non proident, sunt in culpa qui officia deserunt mollit anim id est laborum aute irure dolor aliquip ex ea commodo.</p>
    <div class="go"><svg width="14" height="18" viewBox="0 0 14 18"><path d="M3 2l8 7-8 7" stroke="#fff" stroke-width="3.5" fill="none"/></svg></div>
  </article>
  <article class="abs card" style="left:798px">
    <div class="ph" role="img" aria-label="Arborist in orange gear pruning tree branches" style="background:linear-gradient(160deg,#6f9fcf 0%,#8b7a4e 50%,#4a3a22 100%)"></div>
    <h3>PRUNING TREES</h3>
    <p>Excepteur sint occaecat cupidatat non proident, sunt in culpa qui officia deserunt mollit anim id est laborum aute irure dolor aliquip ex ea commodo.</p>
    <div class="go"><svg width="14" height="18" viewBox="0 0 14 18"><path d="M3 2l8 7-8 7" stroke="#fff" stroke-width="3.5" fill="none"/></svg></div>
  </article>
</section>

<section>
  <div class="abs about" role="img" aria-label="Dusk field with a farm building in the background"></div>
  <div class="abs about-ring"></div>
  <div class="abs about-img" role="img" aria-label="Workers building a concrete block retaining wall"></div>
  <svg class="abs" style="left:116px;top:1518px" width="440" height="150" viewBox="0 0 440 150"><path d="M40 118A220 220 0 0 1 405 110" stroke="#5c9c13" stroke-width="7" fill="none"/></svg>
  <div class="abs about-copy">
    <h2>ABOUT FERNHOLLOW<br>SERVICES</h2>
    <p>Sed ut perspiciatis unde omnis iste natus error sit voluptatem accusantium doloremque laudantium, totam rem aperiam, eaque ipsa quae ab illo inventore veritatis et quasi architecto beatae vitae dicta sunt explicabo. Nemo enim ipsam voluptatem quia voluptas sit aspernatur aut odit aut fugit, sed quia consequuntur magni dolores eos qui ratione voluptatem.</p>
    <div class="btn about-btn">Read More</div>
  </div>
</section>

<section>
  <h2 class="abs sec-title" style="top:2097px">GALLERY</h2>
  <div class="g" role="img" aria-label="Sprayer misting weeds around a young tree" style="left:75px;top:2192px;width:248px;height:188px;background:linear-gradient(160deg,#56603f 0%,#8aa35a 55%,#5e8a2a 100%)"></div>
  <div class="g" role="img" aria-label="Seedlings along irrigation pipe in tilled soil" style="left:337px;top:2192px;width:250px;height:188px;background:linear-gradient(180deg,#c9c46a 0%,#6f9a3a 40%,#4b3a28 75%,#3a2b1e 100%)"></div>
  <div class="g" role="img" aria-label="Worker in hi-vis jacket fixing a metal fence" style="left:75px;top:2396px;width:512px;height:187px;background:linear-gradient(90deg,#2e3a44 0%,#4a5560 45%,#b86a2a 70%,#8aa83a 100%)"></div>
  <div class="g" role="img" aria-label="Yellow excavator digging on a dirt site" style="left:601px;top:2192px;width:512px;height:391px;background:linear-gradient(180deg,#7c8a94 0%,#a09478 40%,#b08a2a 58%,#5a4430 80%,#3a2c20 100%)"></div>
  <div class="btn view">View All</div>
</section>

<section class="abs contact">
  <h2>CONTACT US</h2>
</section>
<div class="abs contact-ph" role="img" aria-label="Tradesman on a phone call beside a mesh fence"></div>
<div class="field" style="left:616px;top:2938px;width:248px;height:48px">First Name</div>
<div class="field" style="left:878px;top:2938px;width:248px;height:48px">Last Name</div>
<div class="field" style="left:616px;top:3001px;width:248px;height:48px">Phone no</div>
<div class="field" style="left:878px;top:3001px;width:248px;height:48px">Subject</div>
<div class="field" style="left:616px;top:3066px;width:510px;height:48px">Email Address</div>
<div class="field" style="left:616px;top:3130px;width:510px;height:86px">Message</div>
<div class="btn dark submit">Submit</div>

<footer class="abs footer">
  <div class="abs brand" style="left:75px;top:127px;gap:10px"><i style="width:18px;height:18px"></i><span style="font-size:22px">Fernhollow Services</span></div>
  <div class="copy">Copyright 2024 Fernhollow Services<br>All Rights Reserved</div>

  <h4 style="left:372px;top:54px">SITE MAP</h4>
  <div class="links" style="left:372px;top:84px">Home<br>About Us<br>Services<br>Gallery<br>Contact Us</div>

  <h4 style="left:617px;top:54px">SERVICES</h4>
  <div class="links" style="left:617px;top:84px">Stock Work<br>Spraying<br>Pastures<br>Building<br>Fencing<br>Water Management<br>General</div>

  <h4 style="left:886px;top:54px">ADDRESS</h4>
  <div class="addr" style="top:86px"><svg width="15" height="12" viewBox="0 0 24 18"><path fill="#5c9c13" d="M0 3l7-3 10 3 7-3v15l-7 3-10-3-7 3z"/></svg><span>48 Totara Lane, Riverbend 7020,<br>Greenvale</span></div>
  <div class="addr" style="top:142px"><svg width="14" height="14" viewBox="0 0 24 24"><path fill="#5c9c13" d="M6.6 10.8a15.1 15.1 0 0 0 6.6 6.6l2.2-2.2a1 1 0 0 1 1-.25 11.4 11.4 0 0 0 3.6.57 1 1 0 0 1 1 1V20a1 1 0 0 1-1 1A17 17 0 0 1 3 4a1 1 0 0 1 1-1h3.5a1 1 0 0 1 1 1c0 1.25.2 2.45.57 3.57a1 1 0 0 1-.25 1z"/></svg><span>+64-555-0142</span></div>
  <div class="addr" style="top:177px"><svg width="14" height="11" viewBox="0 0 24 18"><rect width="24" height="18" rx="2" fill="#5c9c13"/><path d="M1 2l11 8 11-8" stroke="#222" stroke-width="2" fill="none"/></svg><span>hello@fernhollow.example</span></div>
  <div class="social"><i></i><i></i><i></i><i></i><i></i></div>
</footer>

</body>
</html>
```